Business Card - Rebranding for Consulting Firm

We are renaming and rebranding our consulting firm and need to raise the level of quality of our cards as part of that effort. We consult to leading high tech, life science and other innovation sector companies.

Need a two-sided business card design.

Side 1: (a) Company logo (b) tag line: Optimize Your Investment in Talent (c) Name (d) Title (e) Phone 1: Office (f) Phone 2: Mobile (g) email: person@HollowmereAdvisory.com

Side 2: Two lines of text: (a) Growth is Imperative. Change is Constant. Talent Executes Strategy. (b) We help you excel at all three.

Target Market(s)

Business and human resources executives and senior managers

Industry/Entity Type

Management Consulting

Contact Information for Business Card

Font styles to use
Sans Serif

Requirements
Must have
• clean, not too busy, but with a bit of creativity. Stick to the colors used in the attached logo
• appeal to high tech, life science companies
Nice to have
• prefer white background

```html
<!DOCTYPE html>
<html lang="en">
<head>
<meta charset="utf-8">
<title>Hollowmere Advisory – Business Card</title>
<link rel="stylesheet" href="https://fonts.googleapis.com/css2?family=Source+Sans+3:wght@400;600;700&display=swap">
<style>
  :root {
    --backdrop-top: #2a2a2a;
    --backdrop-bottom: #050505;
    --card-white: #ffffff;
    --brand-blue: #0c5f9e;
    --brand-blue-bright: #0b6aa8;
    --text-grey: #3a3a3a;
    --rule-grey: #9fb0bb;
    --on-blue: #ffffff;
  }
  * { margin: 0; padding: 0; box-sizing: border-box; }
  html, body { width: 1200px; height: 900px; overflow: hidden; }
  body {
    background: linear-gradient(to bottom, var(--backdrop-top), var(--backdrop-bottom));
    font-family: "Source Sans 3", "Myriad Pro", sans-serif;
    position: relative;
  }
  .card {
    position: absolute;
    top: 306px;
    height: 271px;
    border-radius: 10px;
  }
  .card--front { left: 150px; width: 438px; background: var(--card-white); }
  .card--back { left: 608px; width: 441px; background: var(--brand-blue-bright); }

  .wordmark {
    position: absolute;
    display: flex;
    align-items: center;
    gap: 10px;
    font-weight: 600;
    white-space: nowrap;
  }
  .wordmark__square { display: block; }
  .card--front .wordmark {
    right: 30px; top: 42px;
    font-size: 27px; color: var(--brand-blue);
  }
  .card--front .wordmark__square { width: 20px; height: 20px; background: var(--brand-blue); }
  .card--back .wordmark {
    left: 0; right: 0; justify-content: center; top: 108px;
    font-size: 36px; color: var(--on-blue);
  }
  .card--back .wordmark__square { width: 26px; height: 26px; background: var(--on-blue); }

  .person { position: absolute; left: 21px; top: 110px; }
  .person__name { font-size: 19px; font-weight: 700; color: var(--brand-blue); line-height: 1.1; }
  .person__title { font-size: 13px; color: var(--text-grey); margin-top: 2px; }

  .divider {
    position: absolute; left: 21px; right: 30px; top: 161px;
    height: 1px; background: var(--rule-grey);
  }

  .tagline {
    position: absolute; left: 22px; top: 198px;
    font-size: 14.5px; line-height: 16px; color: var(--brand-blue);
  }

  .contact {
    position: absolute; right: 25px; top: 181px;
    list-style: none; text-align: right;
    font-size: 12.5px; line-height: 16px; color: var(--text-grey);
  }
  .contact__item { display: flex; justify-content: flex-end; align-items: center; gap: 5px; }
  .contact__icon { width: 9px; height: 9px; fill: var(--brand-blue); flex: none; }

  .statement {
    position: absolute; left: 0; right: 0; top: 188px;
    text-align: center; color: var(--on-blue);
    font-size: 16.5px; line-height: 27px;
  }
</style>
</head>
<body>
  <section class="card card--front" aria-label="Card front">
    <div class="wordmark"><span class="wordmark__square"></span>Hollowmere Advisory</div>

    <div class="person">
      <p class="person__name">Daniel Whitcombe</p>
      <p class="person__title">Managing Director</p>
    </div>

    <div class="divider"></div>

    <p class="tagline">Optimize Your Investment<br>in Talent</p>

    <ul class="contact">
      <li class="contact__item">123-456-7890
        <svg class="contact__icon" viewBox="0 0 10 10" aria-label="Mobile"><rect x="2.5" y="0" width="5" height="10" rx="1"/><rect x="3.5" y="1.2" width="3" height="6.5" fill="#fff"/></svg>
      </li>
      <li class="contact__item">123-456-7890
        <svg class="contact__icon" viewBox="0 0 10 10" aria-label="Office"><path d="M0 3 Q5 0 10 3 L9 4.5 L7 4 L7 3 Q5 2.3 3 3 L3 4 L1 4.5 Z"/><rect x="1.5" y="5" width="7" height="5" rx="0.8"/></svg>
      </li>
      <li class="contact__item">info@youremail.com
        <svg class="contact__icon" viewBox="0 0 10 10" aria-label="Email"><rect x="0" y="2" width="10" height="6.5" rx="0.6"/><path d="M0.5 2.5 L5 6 L9.5 2.5" stroke="#fff" stroke-width="0.9" fill="none"/></svg>
      </li>
      <li class="contact__item">www.HollowmereAdvisory.com
        <svg class="contact__icon" viewBox="0 0 10 10" aria-label="Website"><g fill="none" stroke="#0c5f9e" stroke-width="1.5"><rect x="0.8" y="4.2" width="5" height="3" rx="1.5" transform="rotate(-45 3.3 5.7)"/><rect x="4.2" y="2.8" width="5" height="3" rx="1.5" transform="rotate(-45 6.7 4.3)"/></g></svg>
      </li>
    </ul>
  </section>

  <section class="card card--back" aria-label="Card back">
    <div class="wordmark"><span class="wordmark__square"></span>Hollowmere Advisory</div>
    <p class="statement">
      Growth is Imperative. Change is Constant.<br>
      Talent Executes Strategy. We help you excel at all three
    </p>
  </section>
</body>
</html>
```